Flyer für unser Jubiläumscamp "herbstcamp"

Am 10. - 14.10.2022 und 17. - 21. 10.2022 organisieren wir je eine Woche ein Fussballcamp für Kinder ab 5 Jahren bis 12 Jahren. Ebenfalls feiern wir unser 5 jähriges Jubiläum und bieten deshalb das Camp für 300 statt 350 CHF an.
Für dieses Camp (mit dieses 2 Angeboten) möchten wir einen speziellen Flyer haben. Der Flyedr sollte Kinder freundlich aber auch modern sein. Wir bieten auch ein Leistungs, Girls Only sowie ein Goalicamp. (eventuell ist dies aber zu überlastet dan)
Infos zu unseren Camps: https://balltaler.ch/events/2022-sommercamps-juli/

Kinder, 5-12 Jahre

• Logo, Fun Kidscamp
• Gleiches wie der Flyer angehängt.

```html
<!DOCTYPE html>
<html lang="de">
<head>
<meta charset="utf-8">
<title>Herbstcamp – Fussballcamp für Kinder – Balltaler Kids</title>
<link rel="stylesheet" href="https://fonts.googleapis.com/css2?family=Fredoka:wght@600;700&family=Graduate&family=Roboto:ital,wght@0,400;0,700;1,400&display=swap">
<style>
  :root {
    --orange: #f7891f;
    --orange-dark: #e8761a;
    --yellow: #f6e31c;
    --blue: #4a78c4;
    --green: #1f9a48;
    --ink: #1d2a3a;
    --white: #ffffff;
    --turf-light: #5f9a3a;
    --turf-dark: #2f5a22;
  }
  html, body {
    margin: 0;
    padding: 0;
    width: 927px;
    height: 1200px;
    overflow: hidden;
    background: var(--white);
  }
  .flyer {
    position: relative;
    width: 927px;
    height: 1200px;
    overflow: hidden;
    background: var(--orange);
    font-family: "Roboto", Arial, sans-serif;
    color: var(--white);
  }
  .hero-photo {
    position: absolute;
    left: 0; top: 0;
    width: 927px; height: 597px;
    background:
      radial-gradient(ellipse at 55% 35%, rgba(120,170,90,0.5), transparent 60%),
      linear-gradient(180deg, #6d7a4a 0%, #4d7a34 22%, var(--turf-light) 45%, var(--turf-dark) 100%);
  }
  .graphics {
    position: absolute;
    left: 0; top: 0;
    width: 927px; height: 1200px;
  }
  .title-text {
    font-family: "Fredoka", "Arial Rounded MT Bold", sans-serif;
    font-weight: 700;
    font-size: 80px;
    letter-spacing: 3px;
    fill: var(--white);
  }
  .brand {
    position: absolute;
    left: 363px; top: 455px;
    width: 200px;
    display: flex;
    align-items: center;
    justify-content: center;
    gap: 10px;
    font-family: "Fredoka", "Arial Rounded MT Bold", sans-serif;
    font-weight: 700;
    font-size: 34px;
    color: var(--white);
  }
  .brand-dot {
    width: 22px; height: 22px;
    border-radius: 50%;
    background: var(--orange);
  }
  .date-block .am {
    position: absolute;
    left: 108px; top: 632px;
    font-family: "Graduate", serif;
    font-size: 30px;
    color: var(--yellow);
    -webkit-text-stroke: 1.5px var(--yellow);
    line-height: 1;
  }
  .date-block .day {
    position: absolute;
    left: 106px; top: 664px;
    font-family: "Graduate", serif;
    font-size: 128px;
    line-height: 1;
    color: var(--blue);
    -webkit-text-stroke: 3px var(--ink);
    text-shadow: 5px 4px 0 var(--white);
    letter-spacing: -6px;
  }
  .date-block .divider {
    position: absolute;
    left: 284px; top: 655px;
    width: 3px; height: 142px;
    background: var(--white);
  }
  .date-line {
    position: absolute;
    left: 312px;
    font-family: "Graduate", serif;
    font-size: 58px;
    line-height: 1;
    -webkit-text-stroke: 2.5px var(--ink);
    text-shadow: 3px 3px 0 var(--white);
    white-space: nowrap;
    letter-spacing: 1px;
  }
  .date-line.first { top: 668px; color: var(--green); }
  .date-line.first .und {
    color: var(--yellow);
    -webkit-text-stroke: 2px var(--yellow);
    text-shadow: none;
    margin-left: 10px;
  }
  .date-line.second { top: 735px; color: var(--white); text-shadow: 3px 3px 0 var(--ink); }
  .dash-rule {
    position: absolute;
    border-top: 2px dashed var(--white);
    height: 0;
  }
  .dash-rule.full { left: 97px; top: 829px; width: 733px; }
  .dash-rule.short { left: 285px; top: 988px; width: 545px; }
  .mascot {
    position: absolute;
    left: 105px; top: 832px;
    width: 172px; height: 272px;
    border-radius: 80px 80px 30px 30px;
    background: linear-gradient(180deg, #f5a23a 0%, #f3c43b 35%, #3f6fc0 65%, #f08a25 100%);
    opacity: 0.9;
  }
  .details {
    position: absolute;
    right: 97px; top: 850px;
    width: 580px;
    text-align: right;
    font-size: 14.5px;
    line-height: 20.5px;
  }
  .details p { margin: 0; }
  .details .note { margin-top: 13px; font-style: italic; }
  .infos {
    position: absolute;
    right: 97px; top: 1014px;
    text-align: right;
  }
  .infos h2 {
    margin: 0;
    font-family: "Graduate", serif;
    font-weight: 400;
    font-size: 25px;
    letter-spacing: 4.5px;
    color: var(--yellow);
    -webkit-text-stroke: 1.2px var(--yellow);
    line-height: 1.2;
  }
  .infos .url {
    margin: 6px 0 0;
    font-weight: 700;
    font-size: 22px;
    color: var(--white);
  }
</style>
</head>
<body>
<main class="flyer">
  <div class="hero-photo" role="img" aria-label="Foto: Junge im grünen Trikot schiesst einen Ball auf dem Rasenplatz"></div>

  <svg class="graphics" width="927" height="1200" viewBox="0 0 927 1200" aria-hidden="true">
    <defs>
      <path id="arc-top" d="M150 300 Q465 40 790 300"/>
      <path id="arc-bottom" d="M255 365 Q470 190 685 365"/>
    </defs>
    <rect x="68" y="68" width="792" height="1065" fill="none" stroke="var(--white)" stroke-width="2"/>
    <path d="M68 130 A62 62 0 0 0 130 68" fill="none" stroke="var(--white)" stroke-width="2"/>
    <path d="M798 68 A62 62 0 0 0 860 130" fill="none" stroke="var(--white)" stroke-width="2"/>
    <path d="M213 597 A250 250 0 0 1 713 597" fill="none" stroke="var(--white)" stroke-width="2"/>
    <line x1="68" y1="597" x2="860" y2="597" stroke="var(--white)" stroke-width="2"/>
    <path d="M765 110 Q770 148 808 152 Q770 156 765 194 Q760 156 722 152 Q760 148 765 110Z" fill="var(--orange)"/>
    <path d="M173 365 Q178 402 216 407 Q178 412 173 450 Q168 412 130 407 Q168 402 173 365Z" fill="var(--yellow)"/>
    <rect x="75" y="604" width="778" height="20" fill="var(--orange-dark)"/>
    <rect x="75" y="1106" width="778" height="20" fill="var(--orange-dark)"/>
    <text class="title-text"><textPath href="#arc-top" startOffset="50%" text-anchor="middle">FUSSBALLCAMP</textPath></text>
    <text class="title-text"><textPath href="#arc-bottom" startOffset="50%" text-anchor="middle">FÜR KINDER</textPath></text>
  </svg>

  <div class="brand"><span class="brand-dot"></span>Balltaler</div>

  <section class="date-block">
    <div class="am">AM</div>
    <div class="day">10</div>
    <div class="divider"></div>
    <div class="date-line first">14.10.2022<span class="und">UND</span></div>
    <div class="date-line second">17 - 21.10.2022</div>
  </section>

  <div class="dash-rule full"></div>

  <div class="mascot" role="img" aria-label="Illustration: Löwen-Maskottchen im Fussballdress mit Ball, Daumen hoch"></div>

  <section class="details">
    <p>organisieren wir je eine Woche ein Fussballcamp für Kinder. Ebenfalls feiern<br>
    wir unser <strong>5 jähriges Jubiläum</strong> und bieten deshalb das Camp für<br>
    <strong>300 statt 350 CHF an. (5 Jahre minus 50 CHF)</strong></p>
    <p class="note">Unser Herbstcamp für Kinder von 5 bis 12 Jahren – mit viel Spass,<br>
    Training und Teamgeist. Auch Leistungs-, Girls-Only- und Goalicamps!</p>
  </section>

  <div class="dash-rule short"></div>

  <section class="infos">
    <h2>INFOS ZU UNSEREN CAMPS</h2>
    <p class="url">www.balltaler.ch/events/2022-sommercamps-juli/</p>
  </section>
</main>
</body>
</html>
```